Tallgrove Vale Management

I need a professional website. My current website is tallgrovevalemanagement.com and I hate it. It was created with some AI tool very quickly because I needed a site up and running with no advanced notice. I’m open to all designs .. I trust you, the professionals will deliver the results I’m anxiously awaiting! :)

```html
<!DOCTYPE html>
<html lang="en">
<head>
<meta charset="utf-8">
<title>Tallgrove Vale Management — Contact</title>
<link href="https://fonts.googleapis.com/css2?family=Inter:wght@400;500;600;700&family=Montserrat:wght@800;900&display=swap" rel="stylesheet">
<style>
:root{
  --navy:#1f2d45;
  --navy-deep:#1a263b;
  --red:#c1242d;
  --page:#f6f7f9;
  --white:#ffffff;
  --ink:#1f2d45;
  --muted:#4f5560;
  --soft:#8a93a3;
  --band:#4d4f53;
}
*{margin:0;padding:0;box-sizing:border-box}
html,body{width:1200px;height:967px;overflow:hidden}
body{background:var(--page);font-family:"Inter",sans-serif;color:var(--ink);position:relative}

/* header */
.site-header{position:absolute;left:0;top:0;width:1200px;height:70px;background:var(--white)}
.nav-link{position:absolute;top:29px;font-size:9.4px;font-weight:600;letter-spacing:1.6px;color:#44484f;white-space:nowrap}
.brand{position:absolute;left:555px;top:12px;width:90px;display:flex;flex-direction:column;align-items:center;gap:5px}
.brand-mark{width:12px;height:12px;background:var(--navy)}
.brand-name{font-family:"Montserrat",sans-serif;font-weight:900;font-size:11px;color:var(--navy);letter-spacing:.3px;line-height:12px;text-align:center}
.btn-cta{position:absolute;left:738px;top:18px;width:147px;height:34px;background:var(--red);color:var(--white);font-size:9.4px;font-weight:700;letter-spacing:1.5px;display:flex;align-items:center;justify-content:center;box-shadow:3px 3px 0 var(--navy)}

/* intro */
.eyebrow{position:absolute;left:0;top:130px;width:1200px;display:flex;justify-content:center;align-items:center;gap:10px;font-size:9.5px;font-weight:700;letter-spacing:2.6px;color:#44484f}
.eyebrow i{display:block;width:30px;height:2px;background:var(--red)}
.headline{position:absolute;left:0;top:157px;width:1200px;text-align:center;font-family:"Montserrat",sans-serif;font-weight:900;font-size:38px;line-height:38px;letter-spacing:-1px;color:var(--navy)}
.lede{position:absolute;left:300px;top:247px;width:600px;text-align:center;font-size:13.2px;line-height:21px;color:var(--muted)}

/* info card */
.info-card{position:absolute;left:220px;top:329px;width:305px;height:488px;background:var(--navy);box-shadow:5px 5px 0 var(--navy-deep)}
.info-texture{position:absolute;left:145px;top:0;width:160px;height:160px;background:linear-gradient(135deg,#24334d,#1f2d45)}
.info-brand{position:absolute;left:31px;top:43px;font-family:"Montserrat",sans-serif;font-weight:900;font-size:13px;line-height:15px;color:var(--white)}
.info-rule{position:absolute;left:31px;top:131px;width:40px;height:2px;background:var(--red)}
.contact-item{position:absolute;left:32px;display:flex;gap:12px}
.icon-box{width:26px;height:26px;background:var(--white);box-shadow:2px 2px 0 var(--red);display:flex;align-items:center;justify-content:center;flex:none}
.item-title{font-family:"Montserrat",sans-serif;font-weight:800;font-size:8.6px;color:var(--white);letter-spacing:-.1px;margin-top:2px}
.item-text{font-size:10.6px;line-height:16.3px;color:#dfe3ea;margin-top:6px;white-space:nowrap}

/* form card */
.form-card{position:absolute;left:546px;top:329px;width:434px;height:488px;background:var(--white);border:1px solid var(--navy);box-shadow:5px 5px 0 var(--navy)}
.form-title{position:absolute;left:30px;top:30px;font-family:"Montserrat",sans-serif;font-weight:900;font-size:15.5px;color:var(--navy);letter-spacing:-.3px}
.form-rule{position:absolute;left:30px;top:60px;width:373px;height:1px;background:var(--navy)}
.field-label{position:absolute;font-size:7.6px;font-weight:700;letter-spacing:1.1px;color:#3d424b}
.field{position:absolute;height:35px;border:1.3px solid var(--navy);background:var(--page);font-size:9px;padding:0 11px;display:flex;align-items:center;color:var(--soft)}
.field.select{color:var(--navy);font-weight:600}
.field.area{height:72px;align-items:flex-start;padding-top:12px}
.btn-submit{position:absolute;left:30px;top:422px;width:373px;height:33px;background:var(--red);color:var(--white);font-size:9px;font-weight:700;letter-spacing:1.5px;display:flex;align-items:center;justify-content:center;box-shadow:3px 3px 0 var(--navy)}

/* footer */
.footer-band{position:absolute;left:0;top:877px;width:1200px;height:5px;background:var(--band)}
.site-footer{position:absolute;left:0;top:882px;width:1200px;height:85px;background:var(--navy)}
.foot-text{position:absolute;top:36px;font-size:7.4px;font-weight:600;letter-spacing:1.4px;line-height:10px}
.foot-mark{position:absolute;left:221px;top:39px;width:13px;height:13px;background:var(--white)}
.foot-divider{position:absolute;left:264px;top:36px;width:1px;height:16px;background:#3a4862}
</style>
</head>
<body>

<header class="site-header">
  <span class="nav-link" style="left:360px">SERVICES</span>
  <span class="nav-link" style="left:436px">WHY TALLGROVE</span>
  <div class="brand"><span class="brand-mark"></span><span class="brand-name">TALLGROVE<br>VALE</span></div>
  <span class="nav-link" style="left:663px">CONTACT</span>
  <a class="btn-cta">REQUEST PROPOSAL</a>
</header>

<div class="eyebrow"><i></i>CONNECT<i></i></div>
<h1 class="headline">LET'S DISCUSS YOUR<br>PORTFOLIO.</h1>
<p class="lede">Reach out today to initiate a consultative assessment. We look forward to exploring solutions aligned with your specific investment objectives.</p>

<aside class="info-card">
  <div class="info-texture" role="img" aria-label="Diagonal line texture"></div>
  <div class="info-brand">TALLGROVE<br>VALE</div>
  <div class="info-rule"></div>

  <div class="contact-item" style="top:334px">
    <div class="icon-box">
      <svg width="14" height="11" viewBox="0 0 14 11" fill="none" stroke="#1f2d45" stroke-width="1.3"><rect x="1" y="1" width="12" height="9" rx="1"/><path d="M1.5 1.8 7 6l5.5-4.2"/></svg>
    </div>
    <div>
      <div class="item-title">EMAIL ADDRESS</div>
      <div class="item-text">info@tallgrovevalemanagement.com</div>
    </div>
  </div>

  <div class="contact-item" style="top:392px">
    <div class="icon-box">
      <svg width="11" height="14" viewBox="0 0 11 14" fill="none" stroke="#1f2d45" stroke-width="1.3"><path d="M5.5 13S1 8.4 1 5.3a4.5 4.5 0 0 1 9 0C10 8.4 5.5 13 5.5 13z"/><circle cx="5.5" cy="5.3" r="1.6"/></svg>
    </div>
    <div>
      <div class="item-title">SERVICE AREAS</div>
      <div class="item-text">Proudly managing properties across<br>Greater Cleveland, Akron, and the<br>surrounding Northeast Ohio regions.</div>
    </div>
  </div>
</aside>

<section class="form-card">
  <h2 class="form-title">REQUEST A TAILORED PROPOSAL</h2>
  <div class="form-rule"></div>

  <span class="field-label" style="left:30px;top:82px">FIRST &amp; LAST NAME</span>
  <div class="field" style="left:30px;top:98px;width:176px">John Doe</div>
  <span class="field-label" style="left:227px;top:82px">EMAIL ADDRESS</span>
  <div class="field" style="left:227px;top:98px;width:176px">john@example.com</div>

  <span class="field-label" style="left:30px;top:155px">PHONE NUMBER</span>
  <div class="field" style="left:30px;top:171px;width:176px">(555) 123-4567</div>
  <span class="field-label" style="left:227px;top:155px">UNITS OWNED</span>
  <div class="field select" style="left:227px;top:171px;width:176px">Select units...</div>

  <span class="field-label" style="left:30px;top:227px">PROPERTY LOCATION</span>
  <div class="field select" style="left:30px;top:244px;width:373px">Select location...</div>

  <span class="field-label" style="left:30px;top:300px">HOW CAN WE HELP YOU?</span>
  <div class="field area" style="left:30px;top:316px;width:373px">Tell us about your portfolio goals...</div>

  <a class="btn-submit">SUBMIT REQUEST</a>
</section>

<div class="footer-band"></div>
<footer class="site-footer">
  <span class="foot-mark"></span>
  <span class="foot-divider"></span>
  <span class="foot-text" style="left:285px;color:#c5cbd6">© 2026. ALL RIGHTS<br>RESERVED.</span>
  <span class="foot-text" style="left:444px;color:#717d92">PROUDLY SERVING GREATER CLEVELAND &amp; AKRON,<br>OHIO</span>
  <span class="foot-text" style="left:711px;color:#c5cbd6">PRIVACY</span>
  <span class="foot-text" style="left:770px;color:#c5cbd6">TERMS</span>
  <span class="foot-text" style="left:820px;color:#ffffff;font-weight:700">OWNER<br>PORTAL</span>
  <span class="foot-text" style="left:908px;color:#ffffff;font-weight:700">TENANT<br>PORTAL</span>
</footer>

</body>
</html>
```